Flyer design for retail store owners

i would need to have a flyer design for my retail shop customers to show that I am a mailbox store that has all major shipping vendors to for their shipping needs. Ensuring that they can take advantage of opening a house account at the store and billed monthly, word document has all the details. Please use stock images for the notary public, passport photos, mailbox brass pictures of my actual mailboxes are listed in the pictures. I need to make it POP and WOW these retail store owners as I am using it to advertise the business

```html
<!DOCTYPE html>
<html lang="en">
<head>
<meta charset="utf-8">
<title>Rapid Pack &amp; Send – Mailbox Rental Flyer</title>
<link rel="stylesheet" href="https://fonts.googleapis.com/css2?family=Fira+Sans+Condensed:wght@700;800&family=Nunito+Sans:wght@400;600;700&display=swap">
<style>
  :root {
    --brown: #3b2119;
    --red: #d81f35;
    --peach: #eaa57c;
    --grey-box: #dedcdb;
    --ink: #231f20;
    --paper: #f4f3f3;
    --white: #ffffff;
    --head: "Fira Sans Condensed", sans-serif;
    --body: "Nunito Sans", sans-serif;
  }
  * { box-sizing: border-box; margin: 0; padding: 0; }
  html, body { width: 1200px; height: 853px; overflow: hidden; background: var(--white); }
  body { position: relative; font-family: var(--body); color: var(--ink); }

  .page {
    position: absolute; top: 41px; width: 545px; height: 766px; overflow: hidden;
    background: radial-gradient(circle at 60% 55%, #ffffff 0%, var(--paper) 70%);
    box-shadow: 3px 4px 8px rgba(0,0,0,.35);
  }
  .page--mailbox { left: 42px; }
  .page--shipping { left: 610px; }
  .abs { position: absolute; }

  /* header */
  .header { position: absolute; left: 0; top: 0; width: 545px; height: 207px; }
  .header svg { position: absolute; inset: 0; }
  .header__title { position: absolute; font-family: var(--head); font-weight: 800; line-height: 1; letter-spacing: .3px; white-space: nowrap; }
  .header__title--white { color: var(--white); }
  .header__title--peach { color: var(--peach); }
  .header__lead { position: absolute; color: var(--white); font-size: 10.5px; line-height: 11px; }
  .header__note { position: absolute; font-size: 9.8px; line-height: 10.8px; color: var(--ink); }

  /* feature cards */
  .feature { position: absolute; top: 222px; width: 166px; height: 88px; }
  .feature svg.card { position: absolute; inset: 0; filter: drop-shadow(1px 2px 2px rgba(0,0,0,.18)); }
  .feature__title { position: absolute; left: 50px; top: 5px; font-family: var(--head); font-weight: 800; font-size: 12.5px; line-height: 16px; color: var(--ink); white-space: nowrap; }
  .feature__text { position: absolute; left: 19px; top: 44px; width: 130px; font-size: 8.6px; line-height: 9.8px; }
  .feature__text em { font-style: normal; color: var(--red); }

  .section-title { position: absolute; font-family: var(--head); font-weight: 800; color: var(--red); white-space: nowrap; }
  .promo-box { position: absolute; left: 20px; top: 369px; width: 231px; height: 29px; background: var(--red); color: var(--white); font-size: 8.8px; line-height: 10px; padding: 5px 0 0 13px; }
  .checklist { position: absolute; list-style: none; font-size: 10.2px; line-height: 14.2px; white-space: nowrap; }
  .checklist li { position: relative; padding-left: 17px; }
  .checklist li svg { position: absolute; left: 0; top: 3px; }
  .deals { position: absolute; left: 172px; top: 532px; width: 352px; font-size: 10.1px; line-height: 14.2px; }
  .deals .accent { color: var(--red); }
  .cta { position: absolute; left: 169px; top: 660px; width: 350px; height: 20px; background: var(--red); color: var(--white); font-family: var(--head); font-weight: 800; font-size: 12px; line-height: 20px; padding-left: 9px; white-space: nowrap; }

  .photo { position: absolute; }

  /* footer */
  .footer { position: absolute; left: 0; top: 695px; width: 545px; height: 71px; }
  .footer svg.band { position: absolute; inset: 0; }
  .footer__phone { position: absolute; left: 28px; top: 26px; color: var(--white); font-size: 14.5px; display: flex; align-items: center; gap: 6px; white-space: nowrap; }
  .footer__item { position: absolute; top: 25px; color: var(--white); font-size: 10.8px; line-height: 13px; display: flex; align-items: center; gap: 6px; white-space: nowrap; }

  /* shipping page */
  .service { position: absolute; }
  .service__text { position: absolute; font-size: 10.3px; line-height: 10.8px; color: var(--ink); }
  .service__text .accent { color: var(--red); }
  .service-band { position: absolute; left: 20px; top: 460px; width: 415px; height: 56px; background: var(--red); color: var(--white); font-size: 15px; line-height: 18px; padding: 9px 0 0 21px; white-space: nowrap; }
  .partners-title { position: absolute; left: 41px; top: 562px; font-size: 18.5px; font-weight: 400; color: var(--ink); white-space: nowrap; }
  .partner { position: absolute; top: 596px; width: 103px; height: 49px; }
  .partner svg { position: absolute; inset: 0; filter: drop-shadow(1px 2px 2px rgba(0,0,0,.18)); }
  .partner__name { position: absolute; inset: 0; display: flex; align-items: center; justify-content: center; gap: 4px; padding: 0 10px; text-align: center; font-size: 8.5px; font-weight: 700; line-height: 9.5px; color: var(--brown); }
  .partner__mark { width: 7px; height: 7px; background: var(--red); flex: none; }
</style>
</head>
<body>

<!-- ===== Page 1: mailbox rental ===== -->
<section class="page page--mailbox">
  <header class="header">
    <svg width="545" height="207" viewBox="0 0 545 207">
      <defs>
        <linearGradient id="woodTone" x1="0" y1="0" x2="1" y2="1">
          <stop offset="0" stop-color="#c9a785"/>
          <stop offset=".5" stop-color="#e3cbb0"/>
          <stop offset="1" stop-color="#b89372"/>
        </linearGradient>
      </defs>
      <rect x="240" y="0" width="305" height="207" fill="url(#woodTone)" role="img" aria-label="Photo of a wall of wooden rental mailboxes with small red name tags"/>
      <polygon points="0,0 278,0 232,207 0,207" fill="var(--brown)"/>
      <polygon points="278,0 283,0 237,207 232,207" fill="var(--red)"/>
      <polygon points="0,128 301,128 281,186 0,186" fill="var(--grey-box)"/>
      <polygon points="0,186 281,186 280,189 0,189" fill="var(--red)"/>
      <polygon points="301,128 304,128 283,189 280,189" fill="var(--red)"/>
    </svg>
    <div class="header__title header__title--white" style="left:23px;top:17px;font-size:38px;">RENTING</div>
    <div class="header__title header__title--peach" style="left:23px;top:53px;font-size:30px;">A MAIL BOX</div>
    <p class="header__lead" style="left:24px;top:86px;width:190px;">Is one of the most efficient and cost saving methods for receiving your mail and packages.</p>
    <p class="header__note" style="left:20px;top:136px;width:250px;">Instead of having to worry about private security, weather conditions, sorting, and deliveries; all you have to do is pick-up your mail from our secured facility each day except Sundays.</p>
  </header>

  <!-- feature cards -->
  <article class="feature" style="left:18px;">
    <svg class="card" width="166" height="88" viewBox="0 0 166 88">
      <polygon points="22,0 166,0 148,86 0,86" fill="#fff"/>
      <polygon points="0,86 148,86 147,88 0,88" fill="var(--red)"/>
      <polygon points="148,86 166,0 166,3 149,88" fill="var(--red)"/>
      <polygon points="9,8 46,8 38,30 0,30" fill="var(--peach)"/>
      <g fill="none" stroke="#fff" stroke-width="1.5">
        <rect x="16" y="13" width="16" height="11"/>
        <polyline points="16,13 24,20 32,13"/>
      </g>
    </svg>
    <h3 class="feature__title">YOU WILL GET<br>A NOTIFICATIONG</h3>
    <p class="feature__text">Iwhen mail arrives whether envelope or package, <em>it will be scanned in daily which other mailbox stores do not offer!</em></p>
  </article>

  <article class="feature" style="left:189px;">
    <svg class="card" width="166" height="88" viewBox="0 0 166 88">
      <polygon points="22,0 166,0 148,86 0,86" fill="#fff"/>
      <polygon points="0,86 148,86 147,88 0,88" fill="var(--red)"/>
      <polygon points="148,86 166,0 166,3 149,88" fill="var(--red)"/>
      <polygon points="9,8 46,8 38,30 0,30" fill="var(--peach)"/>
      <g fill="none" stroke="#fff" stroke-width="1.5">
        <rect x="17" y="11" width="11" height="15"/>
        <line x1="19" y1="15" x2="26" y2="15"/><line x1="19" y1="19" x2="26" y2="19"/>
        <line x1="33" y1="11" x2="29" y2="24"/>
      </g>
    </svg>
    <h3 class="feature__title">WE OFFER ONSITE<br>NOTARY PUBLIC</h3>
    <p class="feature__text">With no appointments and onsite Passport Photos</p>
  </article>

  <article class="feature" style="left:359px;">
    <svg class="card" width="166" height="88" viewBox="0 0 166 88">
      <polygon points="22,0 166,0 148,86 0,86" fill="#fff"/>
      <polygon points="0,86 148,86 147,88 0,88" fill="var(--red)"/>
      <polygon points="148,86 166,0 166,3 149,88" fill="var(--red)"/>
      <polygon points="9,8 46,8 38,30 0,30" fill="var(--peach)"/>
      <g fill="#fff">
        <rect x="13" y="14" width="14" height="9"/>
        <polygon points="28,16 33,16 36,20 36,23 28,23"/>
        <circle cx="17" cy="25" r="2"/><circle cx="31" cy="25" r="2"/>
      </g>
    </svg>
    <h3 class="feature__title">SHIPPING</h3>
    <p class="feature__text" style="left:18px;top:44px;">Can ship out same day</p>
  </article>

  <!-- main promotion -->
  <h2 class="section-title" style="left:19px;top:328px;font-size:16px;">MAIN PROMOTION:</h2>
  <p class="abs" style="left:19px;top:352px;font-size:8.6px;white-space:nowrap;">INow renting mailboxes on Maplewood Commons Shopping Center.</p>
  <div class="promo-box">We are offering all Maplewood Commons shopping center owners/employees an exclusive promo deal!</div>
  <h2 class="section-title" style="left:18px;top:407px;font-size:13px;">$12 A MONTH FOR 6-12 MONTHS LEASES!</h2>
  <p class="abs" style="left:22px;top:425px;font-size:12px;font-weight:700;">You get</p>

  <ul class="checklist" style="left:20px;top:443px;">
    <li><svg width="10" height="9" viewBox="0 0 10 9"><rect x=".5" y="1.5" width="7" height="7" fill="none" stroke="var(--red)"/><polyline points="2,5 4,7 9,1" fill="none" stroke="var(--red)" stroke-width="1.4"/></svg>a mailbox in the shop,</li>
    <li><svg width="10" height="9" viewBox="0 0 10 9"><rect x=".5" y="1.5" width="7" height="7" fill="none" stroke="var(--red)"/><polyline points="2,5 4,7 9,1" fill="none" stroke="var(--red)" stroke-width="1.4"/></svg>a book of stamps(20 count),</li>
    <li><svg width="10" height="9" viewBox="0 0 10 9"><rect x=".5" y="1.5" width="7" height="7" fill="none" stroke="var(--red)"/><polyline points="2,5 4,7 9,1" fill="none" stroke="var(--red)" stroke-width="1.4"/></svg>3 notarizations by appointment</li>
  </ul>
  <ul class="checklist" style="left:199px;top:441px;">
    <li><svg width="10" height="9" viewBox="0 0 10 9"><rect x=".5" y="1.5" width="7" height="7" fill="none" stroke="var(--red)"/><polyline points="2,5 4,7 9,1" fill="none" stroke="var(--red)" stroke-width="1.4"/></svg>100 copies of black and white,</li>
    <li><svg width="10" height="9" viewBox="0 0 10 9"><rect x=".5" y="1.5" width="7" height="7" fill="none" stroke="var(--red)"/><polyline points="2,5 4,7 9,1" fill="none" stroke="var(--red)" stroke-width="1.4"/></svg>100 copies of color.</li>
  </ul>
  <p class="abs" style="left:200px;top:472px;font-size:8.8px;font-weight:700;color:var(--red);white-space:nowrap;">Please see associate for sign up!</p>

  <div class="photo" style="left:375px;top:338px;width:147px;height:147px;background:linear-gradient(135deg,#c8955a,#a8773f 55%,#5e3d1d);" role="img" aria-label="Photo of brass-coloured mailbox doors with one door open"></div>

  <div class="photo" style="left:19px;top:507px;width:135px;height:152px;background:linear-gradient(100deg,#9a6c3c,#d5a56c 30%,#c8955c 80%,#a77a48);" role="img" aria-label="Photo of a tall brass mailbox cabinet with many small doors"></div>

  <h2 class="section-title" style="left:172px;top:510px;font-size:13px;">CHECK OUT THESE OTHER DEALS!</h2>
  <div class="deals">
    <p>• As a retail owner, you know how important it is to keep your customers coming back - you will get 20% discount for printing services.</p>
    <p>• We duplicate keys for $2/each, our regular price charge is $4/each.<br>Save up to 50%!</p>
    <p>• Lamination is also discounted at 10% off.</p>
    <p>• 10% off retail supplies ... must be minimum of 10$</p>
    <p>• For house accounts -a 5% discount will be deducted monthly of billing change to invoicing PLUS we're giving another 5% of the discount if you upgrade and sign up for mailbox. <span class="accent">Great right?</span></p>
  </div>
  <div class="cta">TAKE ADVANTAGE OF THIS LIMITED TIME OFFER NOW!</div>

  <footer class="footer">
    <svg class="band" width="545" height="71" viewBox="0 0 545 71">
      <rect x="0" y="6" width="545" height="65" fill="var(--brown)"/>
      <polygon points="0,0 175,0 208,71 0,71" fill="var(--red)"/>
    </svg>
    <div class="footer__phone">
      <svg width="20" height="20" viewBox="0 0 20 20"><circle cx="10" cy="10" r="8.5" fill="none" stroke="#fff" stroke-width="1.6"/><path d="M6 6 l2-1 1.5 3-1 1 c.5 1.2 1.4 2.1 2.6 2.6 l1-1 3 1.5-1 2 c-4 0-8.1-4-8.1-8.1z" fill="#fff"/></svg>
      <span>+1 555 0142 886</span>
    </div>
    <div class="footer__item" style="left:223px;">
      <svg width="15" height="15" viewBox="0 0 15 15" fill="none" stroke="var(--peach)" stroke-width="1.2"><circle cx="7.5" cy="7.5" r="6.5"/><ellipse cx="7.5" cy="7.5" rx="3" ry="6.5"/><line x1="1" y1="7.5" x2="14" y2="7.5"/></svg>
      <span>hello@rapidpack.example<br>www.rapidpack.example</span>
    </div>
    <div class="footer__item" style="left:385px;">
      <svg width="15" height="15" viewBox="0 0 15 15"><path d="M7.5 1 a4.5 4.5 0 0 1 4.5 4.5 c0 3.5-4.5 8.5-4.5 8.5 s-4.5-5-4.5-8.5 A4.5 4.5 0 0 1 7.5 1z" fill="var(--peach)"/><circle cx="7.5" cy="5.5" r="1.6" fill="var(--brown)"/></svg>
      <span>18 Harbor Lane, Eastfield,<br>NY 10990, USA.</span>
    </div>
  </footer>
</section>

<!-- ===== Page 2: shipping services ===== -->
<section class="page page--shipping">
  <header class="header">
    <svg width="545" height="207" viewBox="0 0 545 207">
      <defs>
        <linearGradient id="sealTone" x1="0" y1="0" x2="1" y2="1">
          <stop offset="0" stop-color="#7a4f33"/>
          <stop offset=".45" stop-color="#c9b8a8"/>
          <stop offset=".7" stop-color="#e8e3de"/>
          <stop offset="1" stop-color="#8a6244"/>
        </linearGradient>
      </defs>
      <rect x="200" y="0" width="345" height="207" fill="url(#sealTone)" role="img" aria-label="Photo of a letter closed with a red wax seal and a brass stamp on a wooden table"/>
      <polygon points="0,0 270,0 213,207 0,207" fill="var(--brown)"/>
      <polygon points="270,0 275,0 218,207 213,207" fill="var(--red)"/>
    </svg>
    <div class="header__title header__title--white" style="left:23px;top:29px;font-size:32px;">AT RAPID PACK</div>
    <div class="header__title header__title--peach" style="left:23px;top:68px;font-size:40px;">&amp; SEND,</div>
    <p class="header__lead" style="left:24px;top:141px;width:200px;font-size:12.4px;line-height:12.4px;">Our goal is to make your shipping experience as convenient as possible.</p>
  </header>

  <div class="photo" style="left:156px;top:220px;width:389px;height:336px;background:linear-gradient(180deg,rgba(214,190,160,.35),rgba(214,190,160,.2));" role="img" aria-label="Faint photo of a wall of mailbox doors"></div>

  <!-- service rows -->
  <div class="service" style="left:38px;top:236px;width:400px;height:70px;">
    <svg width="400" height="70" viewBox="0 0 400 70" style="position:absolute;inset:0;">
      <polygon points="86,9 363,9 342,60 86,60" fill="#fff"/>
      <polygon points="0,60 342,60 342,62 0,62" fill="var(--peach)"/>
      <polygon points="342,60 363,9 365,9 344,62" fill="var(--peach)"/>
      <rect x="13" y="0" width="73" height="66" fill="#2f3f70" stroke="var(--red)" role="img" aria-label="Photo of a passport lying on a map"/>
    </svg>
    <p class="service__text" style="left:101px;top:24px;width:240px;">Whether you are shipping packages, documents, or packages, we are here to help.</p>
  </div>

  <div class="service" style="left:38px;top:326px;width:420px;height:100px;">
    <svg width="420" height="100" viewBox="0 0 420 100" style="position:absolute;inset:0;">
      <polygon points="86,8 383,8 363,87 86,87" fill="#fff"/>
      <polygon points="0,87 363,87 363,89 0,89" fill="var(--peach)"/>
      <polygon points="363,87 383,8 385,8 365,89" fill="var(--peach)"/>
      <rect x="13" y="0" width="73" height="98" fill="#b98d62" stroke="var(--red)" role="img" aria-label="Photo of a brown paper parcel with a tag and a magnifying glass"/>
    </svg>
    <p class="service__text" style="left:101px;top:18px;width:225px;">Whether you want to track your package or estimate the price of your package, it is easy for you.</p>
    <p class="service__text" style="left:101px;top:62px;width:260px;"><span class="accent">We are ready to handle all of your postal services!</span></p>
  </div>

  <div class="service-band">Get also the services you need; printing, copying,<br>and stop in to purchase postage or shipping materials.</div>

  <h2 class="partners-title">Service point partners are</h2>

  <div class="partner" style="left:20px;">
    <svg width="103" height="49" viewBox="0 0 103 49"><polygon points="12,0 103,0 91,47 0,47" fill="#fff"/><polygon points="0,47 91,47 91,49 0,49" fill="var(--red)"/><polygon points="91,47 103,0 103,2 92,49" fill="var(--red)"/></svg>
    <div class="partner__name"><span class="partner__mark"></span>Northline Express</div>
  </div>
  <div class="partner" style="left:153px;">
    <svg width="103" height="49" viewBox="0 0 103 49"><polygon points="12,0 103,0 91,47 0,47" fill="#fff"/><polygon points="0,47 91,47 91,49 0,49" fill="var(--red)"/><polygon points="91,47 103,0 103,2 92,49" fill="var(--red)"/></svg>
    <div class="partner__name">Crestway Freight</div>
  </div>
  <div class="partner" style="left:287px;">
    <svg width="103" height="49" viewBox="0 0 103 49"><polygon points="12,0 103,0 91,47 0,47" fill="#fff"/><polygon points="0,47 91,47 91,49 0,49" fill="var(--red)"/><polygon points="91,47 103,0 103,2 92,49" fill="var(--red)"/></svg>
    <div class="partner__name">Parcelpoint Courier</div>
  </div>
  <div class="partner" style="left:423px;">
    <svg width="103" height="49" viewBox="0 0 103 49"><polygon points="12,0 103,0 91,47 0,47" fill="#fff"/><polygon points="0,47 91,47 91,49 0,49" fill="var(--red)"/><polygon points="91,47 103,0 103,2 92,49" fill="var(--red)"/></svg>
    <div class="partner__name">National Mail Service</div>
  </div>

  <footer class="footer">
    <svg class="band" width="545" height="71" viewBox="0 0 545 71">
      <rect x="0" y="6" width="545" height="65" fill="var(--brown)"/>
      <polygon points="0,0 175,0 208,71 0,71" fill="var(--red)"/>
    </svg>
    <div class="footer__phone">
      <svg width="20" height="20" viewBox="0 0 20 20"><circle cx="10" cy="10" r="8.5" fill="none" stroke="#fff" stroke-width="1.6"/><path d="M6 6 l2-1 1.5 3-1 1 c.5 1.2 1.4 2.1 2.6 2.6 l1-1 3 1.5-1 2 c-4 0-8.1-4-8.1-8.1z" fill="#fff"/></svg>
      <span>+1 555 0142 886</span>
    </div>
    <div class="footer__item" style="left:223px;">
      <svg width="15" height="15" viewBox="0 0 15 15" fill="none" stroke="var(--peach)" stroke-width="1.2"><circle cx="7.5" cy="7.5" r="6.5"/><ellipse cx="7.5" cy="7.5" rx="3" ry="6.5"/><line x1="1" y1="7.5" x2="14" y2="7.5"/></svg>
      <span>hello@rapidpack.example<br>www.rapidpack.example</span>
    </div>
    <div class="footer__item" style="left:385px;">
      <svg width="15" height="15" viewBox="0 0 15 15"><path d="M7.5 1 a4.5 4.5 0 0 1 4.5 4.5 c0 3.5-4.5 8.5-4.5 8.5 s-4.5-5-4.5-8.5 A4.5 4.5 0 0 1 7.5 1z" fill="var(--peach)"/><circle cx="7.5" cy="5.5" r="1.6" fill="var(--brown)"/></svg>
      <span>18 Harbor Lane, Eastfield,<br>NY 10990, USA.</span>
    </div>
  </footer>
</section>

</body>
</html>
```